Animated Banner Design for a snacking company

We need a set of banner design to to fit the all the brindle promo spots designs. The banners should be animated and static. Our product has it colors identity that should be used with characters. it should match a movie that explains the product.

The product is subscription serivce that target individual with a healthy lifestyle.

Please visit nine.kovaleth.com and watch the movie on pix cast.

Target Market(s)

Males and Females Age from 18 to 38

Industry/Entity Type

Food Store

Other font styles liked:
• Lato

Colors
3176b5
f37122
5c5c5c

Requirements
Must have
• color scheme to match the video and color codes.
• animation

```html
<!DOCTYPE html>
<html lang="en">
<head>
<meta charset="UTF-8">
<title>Nine Nuts &amp; Seeds – Leaderboard Banner</title>
<link rel="stylesheet" href="https://fonts.googleapis.com/css2?family=Lato:wght@400;700;900&display=swap">
<style>
  :root {
    --brand-orange: #f37122;
    --brand-blue: #3a7dc0;
    --brand-blue-deep: #3176b5;
    --brand-ink: #2c4560;
    --text-light: #ffffff;
    --scene-sky: #eef3f8;
    --scene-wall: #d9e5f0;
    --scene-coat: #f7f9fb;
    --scene-shirt: #b9aed3;
    --scene-desk: #e7c7a8;
  }
  * { margin: 0; padding: 0; box-sizing: border-box; }
  html, body {
    width: 1200px;
    height: 148px;
    overflow: hidden;
    background: #ffffff;
  }
  .banner {
    position: relative;
    width: 1200px;
    height: 148px;
    border: 5px solid var(--brand-orange);
    background: var(--scene-sky);
    overflow: hidden;
    font-family: "Lato", Arial, sans-serif;
  }
  .banner__scene {
    position: absolute;
    left: 0;
    top: 0;
    width: 420px;
    height: 100%;
    background: linear-gradient(100deg,
      var(--scene-sky) 0%,
      var(--scene-wall) 18%,
      var(--scene-coat) 34%,
      var(--scene-wall) 50%,
      var(--scene-shirt) 68%,
      var(--scene-desk) 86%,
      var(--scene-wall) 100%);
  }
  .banner__panel {
    position: absolute;
    top: 0;
    right: 0;
    width: 786px;
    height: 100%;
    background: linear-gradient(180deg, var(--brand-blue) 0%, var(--brand-blue-deep) 100%);
    display: flex;
    flex-direction: column;
    align-items: center;
    justify-content: center;
    color: var(--text-light);
    text-align: center;
    padding-top: 4px;
  }
  .headline {
    display: flex;
    align-items: baseline;
    gap: 12px;
    font-weight: 700;
    font-size: 33px;
    line-height: 1;
    letter-spacing: -0.3px;
  }
  .headline__brand {
    font-weight: 900;
    font-size: 70px;
    line-height: 0.8;
    color: var(--brand-ink);
    letter-spacing: -1.5px;
  }
  .headline__product {
    font-weight: 900;
    font-size: 28px;
    text-transform: uppercase;
  }
  .tagline {
    margin-top: 8px;
    font-weight: 700;
    font-size: 32px;
    line-height: 1.1;
    letter-spacing: -0.3px;
  }
</style>
</head>
<body>
  <div class="banner">
    <div class="banner__scene" role="img" aria-label="Illustration of a doctor in a white coat beside a scientist in a purple shirt looking through a microscope in a bright lab"></div>
    <div class="banner__panel">
      <p class="headline">
        <span class="headline__lead">And a combination of</span>
        <span class="headline__brand">nine</span>
        <span class="headline__product">Nuts &amp; Seeds</span>
      </p>
      <p class="tagline">can help you live longer! and improve your energy!</p>
    </div>
  </div>
</body>
</html>
```